Landing Page for a Social Survey

Hi guys,
we need an elegant landing page for a new project. It's a social survey where users need to answer some questions to participate at a lottery.
I attached an example about what we want. As in the example the design should be very elegant and engage to user to click on the button and take part in the survey.
Also the design should look a bit like lumbrook.
If you have any questions, don't hesitate to ask. I'll try to respond as soon as possible.
Please use the following texts:
Header: "Social Network Umfrage"
Headline above the text: "Herzlichen Glückwunsch"
Text:
"Sie wurden als einer von wenigen Nutzern aus Berlin und Umgebung ausgewählt an unserer Umfrage über Social Networks teilzunehmen.
Die Beantwortung der Fragen dauert nur wenige Sekunden. Als Dankeschön für Ihre Teilnahme können Sie ein Zelvo4, Trenu2 oder Pelwin Slate gewinnen."
Button: "Jetzt teilnehmen"

```html
<!DOCTYPE html>
<html lang="de">
<head>
<meta charset="utf-8">
<title>Social Network Umfrage</title>
<link rel="stylesheet" href="https://fonts.googleapis.com/css2?family=Arimo:wght@400;700&family=Noto+Sans:wght@400;700&display=swap">
<style>
  :root {
    --brand-blue: #3b5998;
    --dialog-head: #6d84b4;
    --dialog-frame: #b4b4b8;
    --dialog-border: #4b4f5a;
    --page-top: #ffffff;
    --page-bottom: #d9deea;
    --text-dark: #1a1a1a;
    --footer-text: #7a7a7a;
    --cta-top: #6fb24c;
    --cta-bottom: #559a35;
    --cta-border: #3f7a26;
    --white: #ffffff;
  }
  * { box-sizing: border-box; margin: 0; padding: 0; }
  html, body { width: 1200px; height: 620px; overflow: hidden; }
  body {
    position: relative;
    font-family: "Noto Sans", Verdana, sans-serif;
    color: var(--text-dark);
    background: var(--white);
  }
  .site-header {
    position: absolute; left: 0; top: 0;
    width: 1200px; height: 81px;
    background: var(--brand-blue);
  }
  .site-title {
    position: absolute; left: 135px; top: 27px;
    font-family: "Arimo", Arial, sans-serif;
    font-weight: 700; font-size: 29px; line-height: 36px;
    color: var(--white); letter-spacing: 0.2px;
  }
  .site-date {
    position: absolute; right: 132px; top: 32px;
    font-family: "Arimo", Arial, sans-serif;
    font-size: 12px; line-height: 16px; color: var(--white);
  }
  .stage {
    position: absolute; left: 0; top: 81px;
    width: 1200px; height: 492px;
    background: linear-gradient(to bottom, var(--page-top) 8%, var(--page-bottom) 100%);
  }
  .dialog-frame {
    position: absolute; left: 319px; top: 199px;
    width: 562px; height: 235px;
    background: var(--dialog-frame);
    border-radius: 9px;
  }
  .dialog {
    position: absolute; left: 10px; top: 10px;
    width: 542px; height: 215px;
    background: var(--white);
    border: 1px solid var(--dialog-border);
  }
  .dialog-title {
    height: 28px;
    background: var(--dialog-head);
    border-bottom: 1px solid var(--brand-blue);
    padding-left: 10px;
    font-weight: 700; font-size: 16.5px; line-height: 27px;
    color: var(--white);
  }
  .dialog-body {
    padding: 14px 12px 0 15px;
    font-size: 14px; line-height: 18px;
  }
  .dialog-body p { margin-bottom: 18px; }
  .cta-button {
    position: absolute; left: 184px; top: 163px;
    width: 171px; height: 31px;
    background: linear-gradient(to bottom, var(--cta-top), var(--cta-bottom));
    border: 1px solid var(--cta-border);
    color: var(--white);
    font-family: "Noto Sans", Verdana, sans-serif;
    font-size: 16px; line-height: 29px; text-align: center;
    text-decoration: none;
    display: block;
  }
  .site-footer {
    position: absolute; left: 0; top: 573px;
    width: 1200px; height: 47px;
    background: var(--white);
  }
  .footer-note {
    position: absolute; left: 144px; top: 15px;
    font-family: "Arimo", Arial, sans-serif;
    font-size: 11px; line-height: 14px; color: var(--footer-text);
  }
</style>
</head>
<body>
  <header class="site-header">
    <h1 class="site-title">Social Network Umfrage</h1>
    <div class="site-date">Juni, 30, 2011</div>
  </header>

  <main class="stage"></main>

  <section class="dialog-frame">
    <div class="dialog">
      <h2 class="dialog-title">Herzlichen Glückwunsch</h2>
      <div class="dialog-body">
        <p>Sie wurden als einer von wenigen Nutzern aus Berlin und Umgebung ausgewählt an unserer Umfrage über Social Networks teilzunehmen.</p>
        <p>Die Beantwortung der Fragen dauert nur wenige Sekunden.</p>
        <p>Als Dankeschön für Ihre Teilnahme können Sie ein Zelvo4, Trenu2 oder Pelwin Slate gewinnen</p>
      </div>
      <a class="cta-button" href="#">Jetzt teilnehmen</a>
    </div>
  </section>

  <footer class="site-footer">
    <p class="footer-note">2011 kelmorapanel.com All rights reserved.</p>
  </footer>
</body>
</html>
```